Online ad and matching banner ad for marketing campaign

We are launching an exciting new site targeted toward real estate professionals and others in the real estate industry. The primary target is realtors.

Our research confirms that many realtors operate with very few branding and marketing assets, tools, or best practices. Many do not have a website, still use Postly or Zintor for professional mail, and have no way to communicate with potential buyers.

Our "Mark Atelier" will offer packages of branding and marketing tools that will help realtors take their earnings to the next level by increasing the way their brand is created and positioned, the tools they use to reach target customers, and the cost effectiveness they enjoy in gaining these tools and access to customized promotional items. Imagine the realtor stepping into the mark atelier with very little branding and marketing success - and leaving with an organized, identifiable brand that they can immediately use to reach customers in a multichannel marketing and messaging solution.

Our website will offer bundles that include a pro, executive, and enterprise offering including everything from domain name registration, hosted email, website design and hosting, social media page creation, cloud based marketing and messaging tools, public relations, and promotional items.

The ad should appeal to the following:

- desire to have a well recognized brand that creates a professional and credible image that can be connected to increasing their number of homes listed and sold.
- desire to grow their current business and income by using simple social media and multichannel marketing and messaging solutions.
- desire to gt what they need fast and cost effectively.

The ad should be bold and easy to understand there is value and opportunity to make more money by visiting our studio site.

Our requirements: Two adds - one with a 5% off coupon and one without a discount -both versions have the following requirements

Once we select a winner - we will request a file including the following per version:

Banner Ad sizes:
-300 Pixels in Width / 250 Pixels in Height
-160 Pixels in Width / 600 Pixels in Height
- Leaderboard: 728 Pixels in Width / 90 Pixels in Height

Online Magazine Ad:
-1/2 Page
Vertical - 3.5” x 9.75”
Horizontal - 7.225” x 4.75”
Island - 4.75” x 7.225”

-1/3 Page
Vertical - 2.375” x 9.75”
Horizontal - 4.625” x 4.75”

Social media Ad:
- 728 x 90 = 65,520 sq pixels
- 300 x 250 = 75,000 sq pixels
- 160 x 600 = 96,000 sq pixels

I have attached our logo to incorporate into the ad. The way we are messaging the studio is:

KMVR Brand Studio (incorporate registered trademark sign) and indicate "powered by" with the attached KMVR logo.

Please send questions if you have any. We will most certainly work with the winner for future work directly.

Target Market(s)

Realtors and real estate professionals

Industry/Entity Type

Real Estate

Requirements
Must have
• Include url:
kmvrbrandstudio.example (currently under construction)

Two versions - one with a 5% off purchase coupon (code save5) and one without any discount.

See the size requirements for both versions as banner ads, online magazine ads, and social media ads.

```html
<!DOCTYPE html>
<html lang="en">
<head>
<meta charset="utf-8">
<title>KMVR Brand Studio – Online Ad and Banner Ad</title>
<link rel="stylesheet" href="https://fonts.googleapis.com/css2?family=Exo+2:wght@700;800&family=Quicksand:wght@500;600&display=swap">
<style>
  :root {
    --page-bg: #ececee;
    --navy: #1f2158;
    --navy-deep: #171a42;
    --navy-mid: #2c3068;
    --lavender: #b9bdd6;
    --ice: #f4f5fb;
    --white: #ffffff;
    --ring: #d7d9e6;
    --label-box: rgba(225, 228, 242, 0.82);
    --label-edge: #c5c8dc;
  }
  * { box-sizing: border-box; margin: 0; padding: 0; }
  html, body { width: 1200px; height: 848px; overflow: hidden; }
  body {
    background: var(--page-bg);
    position: relative;
    font-family: "Exo 2", sans-serif;
  }

  .ad { position: absolute; overflow: hidden; background: var(--navy-deep); }

  /* ---------- Tall ad 160 × 600 format ---------- */
  .ad-tall { left: 322px; top: 48px; width: 252px; height: 700px; }

  .ad-tall .hero {
    position: absolute; left: 0; top: 0; width: 252px; height: 293px;
    background:
      radial-gradient(ellipse at 50% 50%, var(--white) 0%, var(--ice) 35%, transparent 70%),
      linear-gradient(135deg, var(--lavender) 0%, var(--ice) 40%, var(--lavender) 70%, var(--navy-mid) 100%);
  }
  .ad-tall .title-box {
    position: absolute; left: 32px; top: 83px; width: 190px; height: 189px;
    background: var(--label-box); border: 2px solid var(--label-edge);
    display: flex; flex-direction: column; justify-content: center; align-items: center;
  }
  .studio-title {
    color: var(--navy); font-weight: 800; line-height: 0.92;
    text-align: center; letter-spacing: -0.5px;
  }
  .ad-tall .studio-title { font-size: 45px; }

  .powered-band {
    position: absolute; left: 0; width: 100%;
    display: flex; justify-content: center; align-items: center;
    font-family: "Quicksand", sans-serif; font-weight: 600;
    letter-spacing: 4px;
  }
  .ad-tall .powered-band {
    top: 293px; height: 28px; background: var(--navy-mid);
    color: var(--ice); font-size: 18px;
  }

  .logo-zone {
    position: absolute; left: 0; width: 100%;
    display: flex; justify-content: center; align-items: center; gap: 10px;
  }
  .ad-tall .logo-zone {
    top: 321px; height: 134px;
    background:
      radial-gradient(ellipse at 50% 50%, var(--white) 0%, var(--ice) 40%, transparent 80%),
      linear-gradient(160deg, var(--lavender) 0%, var(--ice) 50%, var(--lavender) 100%);
  }
  .logo-dot { border-radius: 50%; background: var(--navy); }
  .ad-tall .logo-dot { width: 34px; height: 34px; }
  .logo-name { color: var(--navy); font-weight: 700; letter-spacing: 1px; }
  .ad-tall .logo-name { font-size: 32px; }

  .offer {
    position: absolute;
    background: linear-gradient(180deg, var(--navy-deep) 0%, var(--navy) 60%, var(--navy-mid) 100%);
  }
  .ad-tall .offer { left: 0; top: 455px; width: 252px; height: 245px; }

  .offer-badge {
    position: absolute; border-radius: 50%;
    border: 3px solid var(--ring);
    display: flex; flex-direction: column; justify-content: center; align-items: center;
    color: var(--white); font-weight: 800; line-height: 0.9; letter-spacing: -1px;
  }
  .offer-badge::before {
    content: ""; position: absolute; inset: 8px; border-radius: 50%;
    border: 2px solid rgba(215, 217, 230, 0.5);
  }
  .ad-tall .offer-badge { left: 31px; top: 22px; width: 190px; height: 190px; font-size: 64px; }

  /* ---------- Square ad 300 × 250 format ---------- */
  .ad-square { left: 621px; top: 262px; width: 308px; height: 256px; }

  .ad-square .hero {
    position: absolute; left: 0; top: 0; width: 161px; height: 256px;
    background:
      radial-gradient(ellipse at 50% 45%, var(--white) 0%, var(--ice) 40%, transparent 75%),
      linear-gradient(150deg, var(--ice) 0%, var(--lavender) 55%, var(--navy-mid) 100%);
  }
  .ad-square .title-box {
    position: absolute; left: 18px; top: 23px; width: 133px; height: 131px;
    background: var(--label-box); border: 2px solid var(--label-edge);
    display: flex; flex-direction: column; justify-content: center; align-items: center;
  }
  .ad-square .studio-title { font-size: 31px; }
  .ad-square .powered-band {
    top: 160px; height: 16px; color: var(--navy-mid); font-size: 13px; letter-spacing: 2px;
  }
  .ad-square .logo-zone { top: 182px; height: 56px; gap: 7px; }
  .ad-square .logo-dot { width: 22px; height: 22px; }
  .ad-square .logo-name { font-size: 21px; }

  .ad-square .offer { left: 161px; top: 0; width: 147px; height: 256px; }
  .ad-square .offer-badge { left: 10px; top: 71px; width: 124px; height: 124px; font-size: 42px; }
</style>
</head>
<body>

  <section class="ad ad-tall" aria-label="KMVR Brand Studio vertical ad">
    <div class="hero" role="img" aria-label="Abstract light shards in lavender and navy"></div>
    <div class="title-box">
      <h1 class="studio-title">KMVR<br>BRAND<br>STUDIO</h1>
    </div>
    <div class="powered-band">powered by</div>
    <div class="logo-zone">
      <span class="logo-dot"></span>
      <span class="logo-name">KMVR</span>
    </div>
    <div class="offer">
      <div class="offer-badge">5%<span>OFF</span></div>
    </div>
  </section>

  <section class="ad ad-square" aria-label="KMVR Brand Studio square banner ad">
    <div class="hero" role="img" aria-label="Abstract light shards in lavender and navy"></div>
    <div class="title-box">
      <h2 class="studio-title">KMVR<br>BRAND<br>STUDIO</h2>
    </div>
    <div class="powered-band" style="width:161px">powered by</div>
    <div class="logo-zone" style="width:161px">
      <span class="logo-dot"></span>
      <span class="logo-name">KMVR</span>
    </div>
    <div class="offer">
      <div class="offer-badge">5%<span>OFF</span></div>
    </div>
  </section>

</body>
</html>
```